Create a book cover for velmora QPL

We are looking for a designer to design a cover for a log book in two versions. The two versions only have a slight difference in page count and text, other than that, it is one design.

The main color is blue. No black, no white except book title and other text. The cover must closely relate to the interior pages provided in the attachment. The style should be simple and modern, no old school graphics and fonts. Apply color psychology in the design. Please be creative and you are allowed to use download templates and graphic elements, but you must provide commercial licenses.

Here are the basic information of the book:
1. Book title: MOTOR CARE TRACKER JOURNAL
2. Book size: 6x9 inches
3. Page count: 61 (version 1) and 73 (version 2)
4. Platform: velmora qpl

Requirement for version 1:
1. Front cover: book title
2. Spine: no book title and author name
3. Back cover: text on the top and pen name logo on the bottom middle
4. Back cover text:
• Your essential tool for tracking vehicle health and maintenance
• Dedicated sections for maintenance schedules and repair history
• Track up to 30 maintenance schedules and repair history
• Easy-to-use tables and clear layouts
• Perfect for all car owners, from enthusiasts to everyday drivers

We hope it helps you keep your vehicle in excellent condition. Please take a moment to leave a positive review on Velmora and share your experience if you find it helpful. Thank you!

Requirement for version 2:
1. Front cover: book title ,text "COLOR PAGES"
4. Back cover text:
• Track up to 36 maintenance schedules and repair history

Export:
1. Cover design in PDF and editable file format.
2. Sources/Commercial licenses for everything you did not create by yourself including fonts.

```html
<!DOCTYPE html>
<html lang="en">
<head>
<meta charset="utf-8">
<title>Motor Care Tracker Journal – Cover</title>
<link rel="stylesheet" href="https://fonts.googleapis.com/css2?family=Bebas+Neue&display=swap">
<style>
  :root {
    --backdrop: #f8dc6a;
    --cover-blue-light: #2f47a3;
    --cover-blue: #233a8f;
    --cover-blue-deep: #1b2a6e;
    --title-white: #f2f2f4;
    --badge-navy: #1c2030;
    --badge-ring: #c9ccd6;
    --art-yellow: #f6c624;
    --art-orange: #f5861a;
  }
  * { margin: 0; padding: 0; box-sizing: border-box; }
  html, body {
    width: 1200px;
    height: 1000px;
    overflow: hidden;
    background: var(--backdrop);
  }
  .canvas {
    position: relative;
    width: 1200px;
    height: 1000px;
    background: var(--backdrop);
  }
  .cover {
    position: absolute;
    left: 316px;
    top: 83px;
    width: 544px;
    height: 842px;
    overflow: hidden;
    background: radial-gradient(ellipse at 40% 45%, var(--cover-blue-light) 0%, var(--cover-blue) 55%, var(--cover-blue-deep) 100%);
    font-family: "Bebas Neue", "Oswald", sans-serif;
    color: var(--title-white);
  }
  .author-badge {
    position: absolute;
    left: 402px;
    top: 30px;
    width: 104px;
    height: 104px;
    border-radius: 50%;
    background: var(--badge-navy);
    border: 3px solid var(--badge-ring);
    display: flex;
    align-items: center;
    justify-content: center;
    text-align: center;
    font-size: 21px;
    line-height: 1;
    letter-spacing: 0.5px;
    color: var(--title-white);
  }
  .hero-art {
    position: absolute;
    left: 0;
    top: 140px;
    width: 494px;
    height: 284px;
    border-radius: 0 60px 16px 0;
    background: linear-gradient(160deg, var(--art-orange) 0%, var(--art-yellow) 60%, #e9a91a 100%);
  }
  .title {
    position: absolute;
    left: 29px;
    top: 465px;
    width: 490px;
    line-height: 1;
    font-weight: 400;
  }
  .title-line { display: block; white-space: nowrap; }
  .title-main { font-size: 190px; line-height: 0.88; letter-spacing: 2px; }
  .title-sub { font-size: 110px; line-height: 0.84; margin-top: -8px; letter-spacing: 0; }
  .title-tag { font-size: 72px; line-height: 0.9; letter-spacing: 17px; margin-top: 7px; }
</style>
</head>
<body>
  <main class="canvas">
    <section class="cover" aria-label="Book cover: Motor Care Tracker Journal">
      <div class="author-badge">DAVIN<br>HOLLOR</div>
      <div class="hero-art" role="img" aria-label="Illustration of a yellow sports car with its orange bonnet raised, shown from the front three-quarter view"></div>
      <h1 class="title">
        <span class="title-line title-main">MOTOR</span>
        <span class="title-line title-sub">CARE TRACKER</span>
        <span class="title-line title-tag">JOURNAL</span>
      </h1>
    </section>
  </main>
</body>
</html>
```